Orvetta Wine Label For Harbor Lemur

Copper Vale Winery is in need of a wine label for new wine being release. This wine will be used as a fundraiser for Harbor Lemur, a chimpanzee santuary in Georgia. The label should reflect a high-end, classy image and the label should suggest the chimp philanthropy without specifically naming the organization (for legal purposes). The label can be a little whimsical without being too cartoonish or child like. This wine will be sold for $30 so it should project a sense of elegance too.
Updates

holiday season makes it difficult to get feedback necessary for approval. just need a few more days...

Industry/Entity Type

Winery

Font styles to use
Sans Serif

Requirements
Must have
• Label should show common design appearance as other labels downloaded.
• Label should be a dark (emerald) green color. Label should have wine name "Orvetta" in center. Label should include an image or silhouette of a chimp on it
Should not have
• no cartoonish images;

```html
<!DOCTYPE html>
<html lang="en">
<head>
<meta charset="utf-8">
<title>Copper Vale Orvetta Red Wine Label</title>
<link rel="stylesheet" href="https://fonts.googleapis.com/css2?family=Federo&family=Marcellus+SC&family=Oswald:wght@400;500&family=Crimson+Text&display=swap">
<style>
  :root {
    --emerald: #0f6b35;
    --emerald-deep: #0a4f27;
    --gold: #b8901c;
    --gold-light: #c9a02a;
    --paper: #ffffff;
    --edge: #555555;
  }
  * { margin: 0; padding: 0; box-sizing: border-box; }
  html, body { width: 1200px; height: 1000px; overflow: hidden; background: var(--paper); }
  .canvas {
    position: relative; width: 1200px; height: 1000px;
    border: 2px solid var(--edge); background: var(--paper);
  }
  .label-art { position: absolute; inset: 0; }
  .text { position: absolute; color: var(--gold-light); }

  .side-brand {
    left: 110px; top: 228px; width: 170px; text-align: center;
    font-family: "Federo", sans-serif; font-size: 22px; line-height: 1; letter-spacing: 1px;
  }
  .side-brand small { display: block; font-size: 13px; letter-spacing: 2px; margin-top: 2px; }
  .chimp-photo { position: absolute; left: 72px; top: 272px; width: 198px; height: 160px; }

  .cause-copy {
    left: 70px; top: 446px; width: 208px;
    font-family: "Crimson Text", serif; font-size: 11.2px; line-height: 1.16;
    text-align: justify;
  }
  .cause-copy p + p { margin-top: 12px; }

  .abv, .volume { top: 750px; font-family: "Oswald", sans-serif; font-size: 15px; letter-spacing: .5px; }
  .abv { left: 312px; }
  .volume { left: 762px; }

  .brand-name {
    left: 400px; top: 420px; width: 402px; text-align: center;
    font-family: "Federo", sans-serif; color: var(--gold);
  }
  .brand-name .line-1 { display: block; font-size: 78px; line-height: 1; letter-spacing: 2px; transform: scaleY(1.25); }
  .brand-name .line-2 { display: flex; align-items: center; justify-content: center; gap: 30px; font-size: 60px; line-height: 1; margin-top: 26px; transform: scaleY(1.2); }
  .brand-name .dot { width: 12px; height: 12px; border-radius: 50%; background: var(--gold); }

  .wine-name {
    left: 440px; top: 648px; width: 322px; text-align: center;
    font-family: "Marcellus SC", serif; color: var(--gold); line-height: 1;
  }
  .wine-name .cuvee { display: block; font-size: 42px; letter-spacing: 1px; }
  .wine-name .style { display: block; font-size: 34px; margin-top: 8px; }

  .warning {
    left: 926px; top: 236px; width: 212px;
    font-family: "Oswald", sans-serif; font-size: 12.8px; line-height: 1.5; text-align: justify;
  }
  .warning h2 { font-size: 15px; font-weight: 500; line-height: 1.2; margin-bottom: 4px; }

  .producer {
    left: 915px; top: 638px; width: 240px; text-align: center;
    font-family: "Oswald", sans-serif; font-size: 15.5px; line-height: 1.25;
  }
  .website { left: 915px; top: 708px; width: 240px; text-align: center; font-family: "Oswald", sans-serif; font-size: 13px; }
  .sulfites { left: 915px; top: 758px; width: 240px; text-align: center; font-family: "Oswald", sans-serif; font-size: 14px; }
</style>
</head>
<body>
<main class="canvas">
  <svg class="label-art" width="1200" height="1000" viewBox="0 0 1200 1000" aria-hidden="true">
    <defs>
      <radialGradient id="emerald-fill" cx="50%" cy="50%" r="60%">
        <stop offset="0" stop-color="#137a3d"/>
        <stop offset="1" stop-color="#0a5128"/>
      </radialGradient>
    </defs>
    <!-- band -->
    <rect x="22" y="192" width="1158" height="616" fill="url(#emerald-fill)" stroke="#123" stroke-width="1"/>
    <rect x="46" y="208" width="1110" height="584" fill="none" stroke="var(--gold)" stroke-width="6"/>
    <!-- diamond -->
    <polygon points="601,85 898,500 601,915 305,500" fill="url(#emerald-fill)"/>
    <polygon points="601,98 889,500 601,902 314,500" fill="none" stroke="var(--gold)" stroke-width="4"/>
    <polygon points="601,119 873,500 601,881 330,500" fill="none" stroke="var(--gold)" stroke-width="2"/>
    <!-- plain mark -->
    <rect x="584" y="226" width="34" height="34" fill="var(--gold)" transform="rotate(45 601 243)"/>
    <!-- plain seal -->
    <circle cx="1030" cy="535" r="56" fill="var(--gold)"/>
    <circle cx="1030" cy="535" r="42" fill="none" stroke="var(--emerald-deep)" stroke-width="2"/>
  </svg>

  <div class="text side-brand">COPPER<small>• VALE •</small></div>
  <div class="chimp-photo" role="img" aria-label="Black and white photograph of two chimpanzees sitting in grass" style="background:linear-gradient(160deg,#d8d8d8,#8a8a8a 55%,#b9b9b9)"></div>

  <div class="text cause-copy">
    <p>A Public awareness campaign design and dedicated to provide lifetime exemplary care to more than 200 chimpanzees.</p>
    <p>September 14, 2015, marked the effective end of unrestricted invasive experiments on chimpanzees in the United States. All chimps, both wild and captive, were listed as endangered under the Endangered Species Act (ESA) on that day, after a decades-long fight to end the use of chimpanzees in laboratory research.</p>
    <p>We support a forever home sanctuary to all of chimpanzees in that laboratory research.</p>
    <p>A portion of this wine sale will go to support this campaign.</p>
    <p>Join the Movement.</p>
  </div>

  <div class="text abv">12.6% ALC./VOL</div>
  <div class="text volume">750ML</div>

  <h1 class="text brand-name">
    <span class="line-1">COPPER</span>
    <span class="line-2"><span class="dot"></span>VALE<span class="dot"></span></span>
  </h1>

  <div class="text wine-name">
    <span class="cuvee">Orvetta</span>
    <span class="style">Red Wine</span>
  </div>

  <section class="text warning">
    <h2>GOVERNMENT WARNING:</h2>
    <p>(1) ACCORDING TO THE SURGEON GENERAL, WOMEN SHOULD NOT DRINK ALCOHOLIC BEVERAGES DURING PREGNANCY BECAUSE OF THE RISK OF BIRTH DEFECTS.</p>
    <p>(2) CONSUMPTION OF ALCOHOLIC BEVERAGES IMPAIRS YOUR ABILITY TO DRIVE A CAR OR OPERATE MACHINERY, AND MAY CAUSE HEALTH PROBLEMS.</p>
  </section>

  <div class="text producer">PRODUCED &amp; BOTTLED AT<br>COPPER VALE, RESORT &amp; SPA<br>RIDGEFORD GA</div>
  <div class="text website">www.coppervalega.com</div>
  <div class="text sulfites">CONTAIN SULFITES</div>
</main>
</body>
</html>
```